Product Label Design

Need a product design for our Epsom salt product, needs to have a luxurious simple feel to it. The picture attached is our brand and wordage on it, the bag we think should be a stand up bag that should be offwhite/creme color. The other picture are products that we like. We updated the packaging to be a Kraft tube box, please see the attached photo for dimensions.

```html
<!DOCTYPE html>
<html lang="en">
<head>
<meta charset="utf-8">
<title>Epsom Salt – Premium Bath Salts Label</title>
<link rel="stylesheet" href="https://fonts.googleapis.com/css2?family=Bodoni+Moda:wght@500&family=Montserrat:wght@600&family=Inter+Tight:wght@500;600&display=swap">
<style>
  :root {
    --stage: #eef1f5;
    --label-base: #ffffff;
    --label-cream: #fbf6ef;
    --brown-deep: #4a2605;
    --brown-gold: #7d4e0c;
    --shadow: rgba(40, 50, 80, 0.16);
  }
  * { margin: 0; padding: 0; box-sizing: border-box; }
  html, body {
    width: 1200px;
    height: 787px;
    overflow: hidden;
    background: var(--stage);
  }
  .canvas {
    position: relative;
    width: 1200px;
    height: 787px;
  }
  .label {
    position: absolute;
    left: 342px;
    top: 43px;
    width: 516px;
    height: 700px;
    background: var(--label-base);
    box-shadow: 0 10px 30px var(--shadow);
    overflow: hidden;
    text-align: center;
    color: var(--brown-deep);
  }
  .label__texture {
    position: absolute;
    inset: 0;
    background: linear-gradient(160deg, var(--label-cream) 0%, var(--label-base) 45%, var(--label-base) 60%, var(--label-cream) 100%);
  }
  .label__title {
    position: absolute;
    left: 0; right: 0;
    top: 140px;
    font-family: "Bodoni Moda", serif;
    font-weight: 500;
    font-size: 47px;
    line-height: 1;
    letter-spacing: -0.01em;
  }
  .label__subtitle {
    position: absolute;
    left: 0; right: 0;
    top: 204px;
    font-family: "Montserrat", sans-serif;
    font-weight: 600;
    font-size: 18px;
    letter-spacing: 0.3em;
    line-height: 1;
    padding-left: 0.3em;
  }
  .label__subtitle .accent { color: var(--brown-gold); }
  .variant {
    position: absolute;
    left: 168px;
    top: 325px;
    width: 180px;
    height: 76px;
    border: 1.4px solid var(--brown-deep);
    border-radius: 18px;
    display: flex;
    align-items: center;
    justify-content: center;
  }
  .variant__name {
    font-family: "Inter Tight", sans-serif;
    font-weight: 600;
    font-size: 25px;
    letter-spacing: -0.02em;
    line-height: 1;
  }
  .label__ingredients {
    position: absolute;
    left: 0; right: 0;
    top: 501px;
    font-family: "Inter Tight", sans-serif;
    font-weight: 500;
    font-size: 17px;
    line-height: 1;
  }
  .label__ingredients .divider { margin: 0 7px; }
  .label__weight {
    position: absolute;
    left: 0; right: 0;
    top: 613px;
    font-family: "Inter Tight", sans-serif;
    font-weight: 500;
    font-size: 17.5px;
    letter-spacing: -0.04em;
    line-height: 1;
  }
</style>
</head>
<body>
  <main class="canvas">
    <section class="label">
      <div class="label__texture" role="img" aria-label="Soft white marble texture with faint warm cream veining"></div>
      <h1 class="label__title">EPSOM SALT</h1>
      <p class="label__subtitle">PREMIUM <span class="accent">BATH SALTS</span></p>
      <div class="variant">
        <p class="variant__name">RECOVERY</p>
      </div>
      <p class="label__ingredients">Magnisium Flakes<span class="divider">|</span>Arnica<span class="divider">|</span>Eucalyptus</p>
      <p class="label__weight">NET WT. 4 OZ (113 G)</p>
    </section>
  </main>
</body>
</html>
```